Personal Development Brand Needs a Workbook Cover Design

We need a clean and sleek cover design for our A4-Sized workbook called the "12-Week Horizon Logbook"

There's around 90 pages in the workbook, if that matters for the spine.

Necessary Elements on the Front Cover:

- Logo
- Title: Peak Lantern Horizon Logbook
- Subtitle: A Simple Workbook to Track Your Transformation
- Author Name: Dale Wrenfold

Elements on Back Cover:

- The Peak Lantern Creed

```html
<!DOCTYPE html>
<html lang="en">
<head>
<meta charset="UTF-8">
<title>Peak Lantern Horizon Logbook – Cover</title>
<link rel="stylesheet" href="https://fonts.googleapis.com/css2?family=Archivo+Black&family=Anton&family=Oswald:wght@500&display=swap">
<style>
  :root {
    --brand-red: #e01f26;
    --ink: #1f1f1f;
    --paper: #ffffff;
    --stone-light: #ececec;
    --stone-mid: #cfcfcf;
    --stone-dark: #a9a9a9;
  }
  html, body {
    margin: 0;
    padding: 0;
    overflow: hidden;
    background: var(--paper);
  }
  .cover {
    position: relative;
    width: 849px;
    height: 1200px;
    overflow: hidden;
    background: var(--stone-light);
  }
  .cover-scene {
    position: absolute;
    inset: 0;
    width: 849px;
    height: 1200px;
  }
  .series-band {
    position: absolute;
    top: 0;
    left: 0;
    width: 849px;
    height: 62px;
    background: var(--brand-red);
    display: flex;
    align-items: center;
    justify-content: center;
  }
  .series-band__label {
    font-family: "Oswald", sans-serif;
    font-weight: 500;
    font-size: 27px;
    letter-spacing: 17px;
    color: var(--paper);
    text-transform: uppercase;
    margin-right: -17px;
  }
  .brand-name {
    position: absolute;
    left: 62px;
    top: 200px;
    width: 722px;
    margin: 0;
    text-align: center;
    font-family: "Archivo Black", sans-serif;
    font-weight: 400;
    font-size: 88px;
    line-height: 1;
    letter-spacing: -3px;
    color: var(--ink);
  }
  .brand-rule {
    position: absolute;
    left: 62px;
    top: 316px;
    width: 722px;
    height: 12px;
    background: var(--brand-red);
  }
  .book-title {
    position: absolute;
    left: 62px;
    top: 334px;
    width: 722px;
    margin: 0;
    text-align: center;
    font-family: "Anton", sans-serif;
    font-weight: 400;
    font-size: 82px;
    line-height: 1.05;
    color: var(--ink);
    text-transform: uppercase;
  }
  .book-subtitle {
    position: absolute;
    left: 258px;
    top: 644px;
    width: 520px;
    margin: 0;
    font-family: "Anton", sans-serif;
    font-weight: 400;
    font-size: 35px;
    line-height: 1.1;
    color: var(--brand-red);
    text-shadow: 2px 2px 0 var(--ink);
  }
  .author-plate {
    position: absolute;
    left: 320px;
    top: 1072px;
    width: 214px;
    height: 58px;
    background: var(--brand-red);
    display: flex;
    align-items: center;
    justify-content: center;
  }
  .author-plate__name {
    font-family: "Anton", sans-serif;
    font-size: 29px;
    color: var(--paper);
    letter-spacing: 0.5px;
  }
</style>
</head>
<body>
  <main class="cover">
    <svg class="cover-scene" viewBox="0 0 849 1200" role="img" aria-label="Photograph: overhead view of a businessman standing beside a large white circular maze on pale grey ground">
      <defs>
        <radialGradient id="stoneGround" cx="0.3" cy="0.45" r="0.9">
          <stop offset="0" stop-color="#f3f3f3"/>
          <stop offset="0.6" stop-color="#dcdcdc"/>
          <stop offset="1" stop-color="#bdbdbd"/>
        </radialGradient>
      </defs>
      <rect x="0" y="0" width="849" height="1200" fill="url(#stoneGround)"/>
    </svg>

    <header class="series-band">
      <span class="series-band__label">12-Week Horizon Logbook</span>
    </header>

    <h1 class="brand-name">Peak Lantern</h1>
    <div class="brand-rule"></div>
    <h2 class="book-title">Horizon Logbook</h2>

    <p class="book-subtitle">A Simple Workbook to Track<br>Your Transformation</p>

    <div class="author-plate">
      <span class="author-plate__name">Dale Wrenfold</span>
    </div>
  </main>
</body>
</html>
```